full stationary design for a modern sleek design company

we are a design company that does modern minimalistic interior design works as well as other design services for high end clients.
we need a full stationary design including and not limited to (double sided business card, letter head, envelopes, documents folder...etc) that reflects the modern style design we do.
sleek modern and minimalistic is the requirements.
Updates

please use the latest attached files as there was a slight modification on the logo Added Wednesday, March 1, 2017

minor update on the logo files in JPG and PSD has been updated kindly follow the new attachments. Added Thursday, March 2, 2017

Target Market(s)

modern minimalist clients

Industry/Entity Type

Design Agency

Requirements
Must have
• the logo
Nice to have
• i like the colors in the colored 3D logo attached
Should not have
• too many colors

```html
<!DOCTYPE html>
<html lang="en">
<head>
<meta charset="utf-8">
<title>Forma Studio – Business Card</title>
<link href="https://fonts.googleapis.com/css2?family=Lato:wght@300;400;700&display=swap" rel="stylesheet">
<style>
  :root {
    --canvas: #e4e4e4;
    --charcoal: #3d3d3d;
    --charcoal-light: #5a5a5a;
    --ink: #3a3a3a;
    --paper: #ffffff;
    --accent: #f7941d;
    --muted: #d8d8d8;
  }
  * { box-sizing: border-box; margin: 0; padding: 0; }
  html, body {
    width: 1200px; height: 702px; overflow: hidden;
    background: var(--canvas);
    font-family: "Lato", Arial, sans-serif;
  }
  .stage {
    position: relative; width: 1200px; height: 702px;
    display: flex; align-items: center; justify-content: center; gap: 50px;
  }
  .card {
    position: relative; width: 520px; height: 297px; overflow: hidden;
    box-shadow: 0 6px 18px rgba(0,0,0,.18);
  }
  /* Back side */
  .card-back {
    background: linear-gradient(135deg, var(--charcoal) 0%, var(--charcoal-light) 100%);
    color: var(--paper);
  }
  .back-mark {
    position: absolute; left: 0; right: 0; top: 102px;
    display: flex; align-items: center; justify-content: center; gap: 12px;
  }
  .back-mark .mark-square { width: 22px; height: 22px; background: var(--accent); }
  .back-mark .mark-name {
    font-size: 54px; font-weight: 700; letter-spacing: 2px; color: var(--paper);
    text-transform: uppercase; line-height: 1;
  }
  .back-web {
    position: absolute; left: 0; right: 0; bottom: 58px; text-align: center;
    font-size: 11px; letter-spacing: .5px; color: var(--muted);
  }
  /* Front side */
  .card-front { background: var(--paper); }
  .front-brand {
    position: absolute; left: 0; right: 0; top: 0; height: 165px;
    display: flex; flex-direction: column; justify-content: center; align-items: flex-end;
    padding-right: 46px;
  }
  .brand-name {
    font-size: 40px; font-weight: 700; color: var(--ink);
    letter-spacing: 3px; text-transform: uppercase; line-height: 1;
  }
  .brand-byline {
    margin-top: 8px; font-size: 17px; font-weight: 400; color: var(--accent);
    letter-spacing: 8px; text-transform: uppercase;
  }
  .front-band {
    position: absolute; left: 0; right: 0; bottom: 0; height: 132px;
    background: linear-gradient(135deg, var(--charcoal-light) 0%, var(--charcoal) 100%);
    color: var(--paper);
  }
  .person { position: absolute; left: 30px; top: 22px; }
  .person-name { font-size: 18px; letter-spacing: .5px; text-transform: uppercase; }
  .person-name strong { font-weight: 700; }
  .person-name span { font-weight: 300; }
  .person-role { font-size: 11px; color: var(--accent); margin-top: 2px; }
  .contact { position: absolute; left: 300px; top: 18px; font-size: 11px; line-height: 1.4; }
  .contact-address { margin-bottom: 10px; }
  .contact-lines {
    border-left: 3px solid var(--accent); padding-left: 8px;
  }
</style>
</head>
<body>
  <main class="stage">
    <section class="card card-back" aria-label="Business card, back">
      <div class="back-mark">
        <span class="mark-square"></span>
        <span class="mark-name">Forma</span>
      </div>
      <p class="back-web">www.formastudio.com</p>
    </section>

    <section class="card card-front" aria-label="Business card, front">
      <div class="front-brand">
        <p class="brand-name">Forma Studio</p>
        <p class="brand-byline">By Lucas Verne</p>
      </div>
      <div class="front-band">
        <div class="person">
          <p class="person-name"><strong>Adrian</strong> <span>Cole</span></p>
          <p class="person-role">Graphic Designer</p>
        </div>
        <div class="contact">
          <p class="contact-address">718 Linden Park Avenue<br>Northgate NY 10482</p>
          <div class="contact-lines">
            <p>000 . 4821 . 7390</p>
            <p>hello@formastudio.com</p>
            <p>www.formastudio.com</p>
          </div>
        </div>
      </div>
    </section>
  </main>
</body>
</html>
```